2014 Wall Calendar Needed

I need a 2014 wall calendar design tweaked for my business Brindle Building Advisors. We are a construction scheduling company you can check out our website www.advisebrindle.example . I had calendars designed last year (attachment #1) that I was pretty happy with but need the following improvements:

1. The Colors on the calendar and the logo must match - Notice the blue on the calendar and the blue on the header are different.

2. The calendar must contain at least 2, preferably 3 months from the end of 2013, and the beginning of 2015. (Some suggested layouts in Attachment #2 and #3)

3. The calendar must have out new "cloud" logo (Attachment #4) and website URL: cloud.advisebrindle.example

4. The calendar should contain the original logo (attachment #5) , and verbiage somewhere:
BRINDLE Building Advisors; Project Solutions; Scheduling, Earned Value Management, Dispute Resolution, 4D Scheduling, Application Cloud Solutions;

5. The contact information:
4372 Harlow Street Suite 500
Silver Spring, MD 20910
Phone 301 555 7186
www.advisebrindle.example

6. The calendar should highlight week numbers and all major American and religious holidays (the holidays on the current calendar are more than enough, as are the week numbers)
Updates

The attachments have been uploaded. Additionally, you cal follow this link to download the attachments referenced in the posting.

 LINK-> https://advisebrindle.filedrop.example/d/k7q2w9184503726615 
 

Target Market(s)

This poster will be sitting in a construction manager's office on the wall and will be used for "at a glance" planning

Industry/Entity Type

Construction

Requirements
Must have
• 1. Contact Information
2. Brindle Logo (attachment #5
3. Brindle Cloud Logo (Attachment #4)
4. 2014 Calendar year
5. at least 2, preferrably 3 months from the surrounding years (Oct Nov Dec 2013 and Jan Feb March of 2015)
6. Major American and Religious holidays
7. Must be able to print on standard poster size: 24X36 INCHES etc.
Nice to have
• Under each month in small font, I would like to have "anticipated weather days *" followed by a number. This number will indicate the anticipated days of inclement weather. I WILL RESEARCH SUPPLY THESE NUMBERS AFTER I CHOOSE THE FINAL DESIGN, these numbers will range from 1-10. At the bottom of the calendar will be an asterisk (*) which references the above statement and reads: "these estimates based on 5 day workweek in the Washington DC/VA area - may vary from contract to contract" this should also be in small font.

```html
<!DOCTYPE html>
<html lang="en">
<head>
<meta charset="utf-8">
<title>Brindle Building Advisors – Calendar 2014</title>
<link rel="stylesheet" href="https://fonts.googleapis.com/css2?family=Arimo:wght@400;700&family=Montserrat:wght@700;800&display=swap">
<style>
  :root {
    --frame: #1f3f8f;
    --paper: #ffffff;
    --brand-blue: #2a6cc0;
    --brand-orange: #e89a2c;
    --ink: #111111;
    --muted: #444444;
    --sand: #f5d9a6;
    --sky: #c3dcf2;
    --bar-dark: #151515;
    --bar-blue: #2a6cc0;
    --label: #ffffff;
    --line: #8a8a8a;
  }
  * { box-sizing: border-box; margin: 0; padding: 0; }
  html, body { width: 900px; height: 1200px; overflow: hidden; }
  body { background: var(--frame); font-family: "Arimo", Arial, sans-serif; color: var(--ink); }
  .poster { position: absolute; left: 10px; top: 0; width: 880px; height: 1200px; background: var(--paper); }

  .masthead { position: absolute; left: 0; top: 0; width: 100%; height: 100px; }
  .brand-cloud {
    position: absolute; left: 30px; top: 34px; display: flex; align-items: center; gap: 10px;
    font-family: "Montserrat", sans-serif; font-weight: 800; font-size: 24px; color: var(--brand-blue);
  }
  .brand-cloud .dot { width: 24px; height: 24px; border-radius: 50%; background: var(--brand-blue); }
  .title {
    position: absolute; left: 290px; top: 34px; width: 300px; text-align: center;
    font-family: "Montserrat", sans-serif; font-weight: 700; font-size: 27px; letter-spacing: 1px;
  }
  .brand-main {
    position: absolute; right: 24px; top: 28px; width: 250px; display: flex; align-items: center; gap: 10px;
    font-family: "Montserrat", sans-serif; font-weight: 800; font-size: 16px; line-height: 1.15; color: var(--brand-blue);
  }
  .brand-main .square { flex: none; width: 34px; height: 34px; background: var(--brand-orange); }

  .months {
    position: absolute; left: 22px; top: 100px; width: 836px; height: 986px;
    display: grid; grid-template-columns: repeat(3, 1fr); grid-template-rows: repeat(6, 1fr);
    column-gap: 22px; row-gap: 10px;
  }
  .month { display: flex; flex-direction: column; border: 1px solid var(--line); background: var(--sand); min-height: 0; }
  .month--sky { background: var(--sky); }
  .month__bar {
    display: flex; justify-content: space-between; align-items: center; flex: none;
    height: 18px; padding: 0 7px; background: var(--bar-dark); color: var(--label);
    font-size: 11px; font-weight: 700;
  }
  .month--sky .month__bar { background: var(--bar-blue); }
  .month__weeks { font-size: 8px; font-weight: 400; }
  .month__days {
    flex: none; display: grid; grid-template-columns: repeat(7, 1fr); background: #ffffff;
    font-size: 7px; font-weight: 700; text-align: center; padding: 1px 4px; border-bottom: 1px solid var(--line);
  }
  .month__dates {
    flex: 1; min-height: 0; display: grid; grid-template-columns: repeat(7, 1fr); grid-template-rows: repeat(6, 1fr);
    font-size: 13px; font-weight: 700; padding: 1px 4px;
  }
  .month__dates span { display: flex; align-items: center; justify-content: center; }
  .month__dates .hol { color: #ffffff; }
  .month__dates .hol::before {
    content: ""; position: absolute; width: 20px; height: 16px; border-radius: 3px; background: var(--brand-orange); z-index: -1;
  }
  .month__dates span { position: relative; z-index: 0; }
  .month__holidays {
    flex: none; height: 13px; padding: 0 6px; font-size: 7.5px; line-height: 13px; color: var(--muted);
    border-top: 1px solid rgba(0,0,0,.15); white-space: nowrap; overflow: hidden;
  }

  .contact {
    position: absolute; left: 22px; top: 1096px; width: 836px; height: 88px;
    display: flex; justify-content: space-between; align-items: center; gap: 30px;
    border-top: 2px solid var(--brand-blue); padding-top: 6px;
  }
  .contact__services { width: 470px; font-size: 11px; line-height: 1.45; color: var(--muted); }
  .contact__services strong { display: block; font-family: "Montserrat", sans-serif; font-size: 13px; color: var(--brand-blue); }
  .contact__details { text-align: right; font-size: 11px; line-height: 1.45; color: var(--ink); }
  .contact__details .web { color: var(--brand-blue); font-weight: 700; }

  .footer-band {
    position: absolute; left: 0; bottom: 0; width: 100%; height: 10px;
    background: linear-gradient(90deg, var(--brand-blue) 0%, var(--frame) 50%, var(--brand-orange) 100%);
  }
</style>
</head>
<body>
<div class="poster">
  <header class="masthead">
    <div class="brand-cloud"><span class="dot"></span>BRINDLE cloud</div>
    <h1 class="title">CALENDAR 2014</h1>
    <div class="brand-main"><span class="square"></span><span>BRINDLE<br>BUILDING ADVISORS</span></div>
  </header>

  <main class="months">
    <section class="month"><div class="month__bar">OCTOBER 2013<span class="month__weeks">weeks 40-44</span></div><div class="month__days"><span>SUN</span><span>MON</span><span>TUE</span><span>WED</span><span>THU</span><span>FRI</span><span>SAT</span></div><div class="month__dates"><span></span><span></span><span>1</span><span>2</span><span>3</span><span>4</span><span>5</span><span>6</span><span>7</span><span>8</span><span>9</span><span>10</span><span>11</span><span>12</span><span>13</span><span class="hol">14</span><span>15</span><span>16</span><span>17</span><span>18</span><span>19</span><span>20</span><span>21</span><span>22</span><span>23</span><span>24</span><span>25</span><span>26</span><span>27</span><span>28</span><span>29</span><span>30</span><span class="hol">31</span></div><div class="month__holidays">14 Columbus Day · 31 Halloween</div></section>

    <section class="month month--sky"><div class="month__bar">NOVEMBER 2013<span class="month__weeks">weeks 44-48</span></div><div class="month__days"><span>SUN</span><span>MON</span><span>TUE</span><span>WED</span><span>THU</span><span>FRI</span><span>SAT</span></div><div class="month__dates"><span></span><span></span><span></span><span></span><span></span><span>1</span><span>2</span><span>3</span><span>4</span><span>5</span><span>6</span><span>7</span><span>8</span><span>9</span><span>10</span><span class="hol">11</span><span>12</span><span>13</span><span>14</span><span>15</span><span>16</span><span>17</span><span>18</span><span>19</span><span>20</span><span>21</span><span>22</span><span>23</span><span>24</span><span>25</span><span>26</span><span>27</span><span class="hol">28</span><span>29</span><span>30</span></div><div class="month__holidays">11 Veterans Day · 28 Thanksgiving · 28 Hanukkah</div></section>

    <section class="month"><div class="month__bar">DECEMBER 2013<span class="month__weeks">weeks 49-1</span></div><div class="month__days"><span>SUN</span><span>MON</span><span>TUE</span><span>WED</span><span>THU</span><span>FRI</span><span>SAT</span></div><div class="month__dates"><span>1</span><span>2</span><span>3</span><span>4</span><span>5</span><span>6</span><span>7</span><span>8</span><span>9</span><span>10</span><span>11</span><span>12</span><span>13</span><span>14</span><span>15</span><span>16</span><span>17</span><span>18</span><span>19</span><span>20</span><span>21</span><span>22</span><span>23</span><span>24</span><span class="hol">25</span><span>26</span><span>27</span><span>28</span><span>29</span><span>30</span><span>31</span></div><div class="month__holidays">25 Christmas Day</div></section>

    <section class="month"><div class="month__bar">JANUARY 2014<span class="month__weeks">weeks 1-5</span></div><div class="month__days"><span>SUN</span><span>MON</span><span>TUE</span><span>WED</span><span>THU</span><span>FRI</span><span>SAT</span></div><div class="month__dates"><span></span><span></span><span></span><span class="hol">1</span><span>2</span><span>3</span><span>4</span><span>5</span><span>6</span><span>7</span><span>8</span><span>9</span><span>10</span><span>11</span><span>12</span><span>13</span><span>14</span><span>15</span><span>16</span><span>17</span><span>18</span><span>19</span><span class="hol">20</span><span>21</span><span>22</span><span>23</span><span>24</span><span>25</span><span>26</span><span>27</span><span>28</span><span>29</span><span>30</span><span>31</span></div><div class="month__holidays">1 New Year's Day · 20 M. L. King Jr. Day</div></section>

    <section class="month month--sky"><div class="month__bar">FEBRUARY 2014<span class="month__weeks">weeks 5-9</span></div><div class="month__days"><span>SUN</span><span>MON</span><span>TUE</span><span>WED</span><span>THU</span><span>FRI</span><span>SAT</span></div><div class="month__dates"><span></span><span></span><span></span><span></span><span></span><span></span><span>1</span><span>2</span><span>3</span><span>4</span><span>5</span><span>6</span><span>7</span><span>8</span><span>9</span><span>10</span><span>11</span><span>12</span><span>13</span><span class="hol">14</span><span>15</span><span>16</span><span class="hol">17</span><span>18</span><span>19</span><span>20</span><span>21</span><span>22</span><span>23</span><span>24</span><span>25</span><span>26</span><span>27</span><span>28</span></div><div class="month__holidays">14 Valentine's Day · 17 Presidents' Day</div></section>

    <section class="month"><div class="month__bar">MARCH 2014<span class="month__weeks">weeks 9-14</span></div><div class="month__days"><span>SUN</span><span>MON</span><span>TUE</span><span>WED</span><span>THU</span><span>FRI</span><span>SAT</span></div><div class="month__dates"><span></span><span></span><span></span><span></span><span></span><span></span><span>1</span><span>2</span><span>3</span><span>4</span><span class="hol">5</span><span>6</span><span>7</span><span>8</span><span>9</span><span>10</span><span>11</span><span>12</span><span>13</span><span>14</span><span>15</span><span>16</span><span class="hol">17</span><span>18</span><span>19</span><span>20</span><span>21</span><span>22</span><span>23</span><span>24</span><span>25</span><span>26</span><span>27</span><span>28</span><span>29</span><span>30</span><span>31</span></div><div class="month__holidays">5 Ash Wednesday · 17 St. Patrick's Day</div></section>

    <section class="month"><div class="month__bar">APRIL 2014<span class="month__weeks">weeks 14-18</span></div><div class="month__days"><span>SUN</span><span>MON</span><span>TUE</span><span>WED</span><span>THU</span><span>FRI</span><span>SAT</span></div><div class="month__dates"><span></span><span></span><span>1</span><span>2</span><span>3</span><span>4</span><span>5</span><span>6</span><span>7</span><span>8</span><span>9</span><span>10</span><span>11</span><span>12</span><span>13</span><span>14</span><span class="hol">15</span><span>16</span><span>17</span><span class="hol">18</span><span>19</span><span class="hol">20</span><span>21</span><span>22</span><span>23</span><span>24</span><span>25</span><span>26</span><span>27</span><span>28</span><span>29</span><span>30</span></div><div class="month__holidays">15 Passover · 18 Good Friday · 20 Easter</div></section>

    <section class="month month--sky"><div class="month__bar">MAY 2014<span class="month__weeks">weeks 18-22</span></div><div class="month__days"><span>SUN</span><span>MON</span><span>TUE</span><span>WED</span><span>THU</span><span>FRI</span><span>SAT</span></div><div class="month__dates"><span></span><span></span><span></span><span></span><span>1</span><span>2</span><span>3</span><span>4</span><span>5</span><span>6</span><span>7</span><span>8</span><span>9</span><span>10</span><span class="hol">11</span><span>12</span><span>13</span><span>14</span><span>15</span><span>16</span><span>17</span><span>18</span><span>19</span><span>20</span><span>21</span><span>22</span><span>23</span><span>24</span><span>25</span><span class="hol">26</span><span>27</span><span>28</span><span>29</span><span>30</span><span>31</span></div><div class="month__holidays">11 Mother's Day · 26 Memorial Day</div></section>

    <section class="month"><div class="month__bar">JUNE 2014<span class="month__weeks">weeks 23-27</span></div><div class="month__days"><span>SUN</span><span>MON</span><span>TUE</span><span>WED</span><span>THU</span><span>FRI</span><span>SAT</span></div><div class="month__dates"><span>1</span><span>2</span><span>3</span><span>4</span><span>5</span><span>6</span><span>7</span><span>8</span><span>9</span><span>10</span><span>11</span><span>12</span><span>13</span><span>14</span><span class="hol">15</span><span>16</span><span>17</span><span>18</span><span>19</span><span>20</span><span>21</span><span>22</span><span>23</span><span>24</span><span>25</span><span>26</span><span>27</span><span>28</span><span>29</span><span>30</span></div><div class="month__holidays">15 Father's Day</div></section>

    <section class="month"><div class="month__bar">JULY 2014<span class="month__weeks">weeks 27-31</span></div><div class="month__days"><span>SUN</span><span>MON</span><span>TUE</span><span>WED</span><span>THU</span><span>FRI</span><span>SAT</span></div><div class="month__dates"><span></span><span></span><span>1</span><span>2</span><span>3</span><span class="hol">4</span><span>5</span><span>6</span><span>7</span><span>8</span><span>9</span><span>10</span><span>11</span><span>12</span><span>13</span><span>14</span><span>15</span><span>16</span><span>17</span><span>18</span><span>19</span><span>20</span><span>21</span><span>22</span><span>23</span><span>24</span><span>25</span><span>26</span><span>27</span><span>28</span><span>29</span><span>30</span><span>31</span></div><div class="month__holidays">4 Independence Day</div></section>

    <section class="month month--sky"><div class="month__bar">AUGUST 2014<span class="month__weeks">weeks 31-36</span></div><div class="month__days"><span>SUN</span><span>MON</span><span>TUE</span><span>WED</span><span>THU</span><span>FRI</span><span>SAT</span></div><div class="month__dates"><span></span><span></span><span></span><span></span><span></span><span>1</span><span>2</span><span>3</span><span>4</span><span>5</span><span>6</span><span>7</span><span>8</span><span>9</span><span>10</span><span>11</span><span>12</span><span>13</span><span>14</span><span>15</span><span>16</span><span>17</span><span>18</span><span>19</span><span>20</span><span>21</span><span>22</span><span>23</span><span>24</span><span>25</span><span>26</span><span>27</span><span>28</span><span>29</span><span>30</span><span>31</span></div><div class="month__holidays">No major holidays</div></section>

    <section class="month"><div class="month__bar">SEPTEMBER 2014<span class="month__weeks">weeks 36-40</span></div><div class="month__days"><span>SUN</span><span>MON</span><span>TUE</span><span>WED</span><span>THU</span><span>FRI</span><span>SAT</span></div><div class="month__dates"><span></span><span class="hol">1</span><span>2</span><span>3</span><span>4</span><span>5</span><span>6</span><span>7</span><span>8</span><span>9</span><span>10</span><span>11</span><span>12</span><span>13</span><span>14</span><span>15</span><span>16</span><span>17</span><span>18</span><span>19</span><span>20</span><span>21</span><span>22</span><span>23</span><span>24</span><span class="hol">25</span><span>26</span><span>27</span><span>28</span><span>29</span><span>30</span></div><div class="month__holidays">1 Labor Day · 25 Rosh Hashanah</div></section>

    <section class="month"><div class="month__bar">OCTOBER 2014<span class="month__weeks">weeks 40-44</span></div><div class="month__days"><span>SUN</span><span>MON</span><span>TUE</span><span>WED</span><span>THU</span><span>FRI</span><span>SAT</span></div><div class="month__dates"><span></span><span></span><span></span><span>1</span><span>2</span><span>3</span><span class="hol">4</span><span>5</span><span>6</span><span>7</span><span>8</span><span>9</span><span>10</span><span>11</span><span>12</span><span class="hol">13</span><span>14</span><span>15</span><span>16</span><span>17</span><span>18</span><span>19</span><span>20</span><span>21</span><span>22</span><span>23</span><span>24</span><span>25</span><span>26</span><span>27</span><span>28</span><span>29</span><span>30</span><span class="hol">31</span></div><div class="month__holidays">4 Yom Kippur · 13 Columbus Day · 31 Halloween</div></section>

    <section class="month month--sky"><div class="month__bar">NOVEMBER 2014<span class="month__weeks">weeks 44-49</span></div><div class="month__days"><span>SUN</span><span>MON</span><span>TUE</span><span>WED</span><span>THU</span><span>FRI</span><span>SAT</span></div><div class="month__dates"><span></span><span></span><span></span><span></span><span></span><span></span><span>1</span><span>2</span><span>3</span><span>4</span><span>5</span><span>6</span><span>7</span><span>8</span><span>9</span><span>10</span><span class="hol">11</span><span>12</span><span>13</span><span>14</span><span>15</span><span>16</span><span>17</span><span>18</span><span>19</span><span>20</span><span>21</span><span>22</span><span>23</span><span>24</span><span>25</span><span>26</span><span class="hol">27</span><span>28</span><span>29</span><span>30</span></div><div class="month__holidays">11 Veterans Day · 27 Thanksgiving</div></section>

    <section class="month"><div class="month__bar">DECEMBER 2014<span class="month__weeks">weeks 49-1</span></div><div class="month__days"><span>SUN</span><span>MON</span><span>TUE</span><span>WED</span><span>THU</span><span>FRI</span><span>SAT</span></div><div class="month__dates"><span></span><span>1</span><span>2</span><span>3</span><span>4</span><span>5</span><span>6</span><span>7</span><span>8</span><span>9</span><span>10</span><span>11</span><span>12</span><span>13</span><span>14</span><span>15</span><span>16</span><span class="hol">17</span><span>18</span><span>19</span><span>20</span><span>21</span><span>22</span><span>23</span><span>24</span><span class="hol">25</span><span>26</span><span>27</span><span>28</span><span>29</span><span>30</span><span>31</span></div><div class="month__holidays">17 Hanukkah · 25 Christmas Day</div></section>

    <section class="month"><div class="month__bar">JANUARY 2015<span class="month__weeks">weeks 1-5</span></div><div class="month__days"><span>SUN</span><span>MON</span><span>TUE</span><span>WED</span><span>THU</span><span>FRI</span><span>SAT</span></div><div class="month__dates"><span></span><span></span><span></span><span></span><span class="hol">1</span><span>2</span><span>3</span><span>4</span><span>5</span><span>6</span><span>7</span><span>8</span><span>9</span><span>10</span><span>11</span><span>12</span><span>13</span><span>14</span><span>15</span><span>16</span><span>17</span><span>18</span><span class="hol">19</span><span>20</span><span>21</span><span>22</span><span>23</span><span>24</span><span>25</span><span>26</span><span>27</span><span>28</span><span>29</span><span>30</span><span>31</span></div><div class="month__holidays">1 New Year's Day · 19 M. L. King Jr. Day</div></section>

    <section class="month month--sky"><div class="month__bar">FEBRUARY 2015<span class="month__weeks">weeks 6-9</span></div><div class="month__days"><span>SUN</span><span>MON</span><span>TUE</span><span>WED</span><span>THU</span><span>FRI</span><span>SAT</span></div><div class="month__dates"><span>1</span><span>2</span><span>3</span><span>4</span><span>5</span><span>6</span><span>7</span><span>8</span><span>9</span><span>10</span><span>11</span><span>12</span><span>13</span><span class="hol">14</span><span>15</span><span class="hol">16</span><span>17</span><span class="hol">18</span><span>19</span><span>20</span><span>21</span><span>22</span><span>23</span><span>24</span><span>25</span><span>26</span><span>27</span><span>28</span></div><div class="month__holidays">14 Valentine's · 16 Presidents' Day · 18 Ash Wed.</div></section>

    <section class="month"><div class="month__bar">MARCH 2015<span class="month__weeks">weeks 10-14</span></div><div class="month__days"><span>SUN</span><span>MON</span><span>TUE</span><span>WED</span><span>THU</span><span>FRI</span><span>SAT</span></div><div class="month__dates"><span>1</span><span>2</span><span>3</span><span>4</span><span>5</span><span>6</span><span>7</span><span>8</span><span>9</span><span>10</span><span>11</span><span>12</span><span>13</span><span>14</span><span>15</span><span>16</span><span class="hol">17</span><span>18</span><span>19</span><span>20</span><span>21</span><span>22</span><span>23</span><span>24</span><span>25</span><span>26</span><span>27</span><span>28</span><span>29</span><span>30</span><span>31</span></div><div class="month__holidays">17 St. Patrick's Day</div></section>
  </main>

  <footer class="contact">
    <div class="contact__services">
      <strong>BRINDLE Building Advisors — Project Solutions</strong>
      Scheduling · Earned Value Management · Dispute Resolution · 4D Scheduling · Application Cloud Solutions
    </div>
    <div class="contact__details">
      4372 Harlow Street Suite 500<br>
      Silver Spring, MD 20910 · Phone 301 555 7186<br>
      <span class="web">www.advisebrindle.example</span> · <span class="web">cloud.advisebrindle.example</span>
    </div>
  </footer>

  <div class="footer-band"></div>
</div>
</body>
</html>
```